Stylish, Masculine Design - Men's Clothing

Granary Coat Mart is a 14,000 square foot warehouse outlet store open to the public since 2005. 50+ brands. Well-known designer brand names and private labels. 30-80% off retail everyday. Lowest prices guaranteed. Average suit price $150. Average shirt price $20. One-stop shop shopping. Men's suits, tuxedos, tuxedo rentals, dress shirts, ties, dress shoes, boy's suits and tuxedos, clergy robes, clergy shirts, cologne, loungewear. Slim fits (Prom Dance), business styles, "church" fashion, security-related uniform. Alterations done by expert tailors on premises for an extra charge.
The final design for both business card and logo should portray stylishness and masculinity.
Updates
We will be changing our name. Details below.New name: Warehouse Suit & TuxFormer name: Granary Coat Mart Added Monday, December 26, 2016
Target Market(s)
Gender: 80% Male, 15% Female, 5% Transgender
Location: 80% 10 Mile Radius, 20% >10 Mile Radius
Age: 17-18 (Primarily prom), 18-35 (Primarily Interviews and Weddings), 36-70 (primarily Church and events)
Race: African-American 50%, Latino-American 20%, White 15%, 10% Asian 5% Other
Religions: Christian 50%, 20% Catholic, 10% Mormon, 20% Other/None
Occupation: Local government 40%, Large corporation employee 20%, Small business employee 10%, Small business owner 10%, 20% Unemployed (high school, college)
Education: High School or equivalent 40%, College 30%, Some College 20%, Masters/Doctors 10%
Industry/Entity Type
Retail
Contact Information for Business Card
Name: Peter Olund
Title: Sales Associate
Address: 418 E. Mirabeth Ave. Gardena, CA 90247
Phone Number: 310.555.0182
Slogan: Warehouse Selection. Outlet Prices, Outstanding Service
www.granarycoatmart.example
Logo Text
GCM (Acronym for Granary Coat Mart) or Image
Requirements
Must have
- Easy to read
- Visually appealing

```html
<!DOCTYPE html>
<html lang="en">
<head>
<meta charset="utf-8">
<title>Granary Coat Mart – Business Card</title>
<link rel="stylesheet" href="https://fonts.googleapis.com/css2?family=Source+Sans+3:wght@400;600;700&display=swap">
<style>
  :root {
    --backdrop: #d9d6d7;
    --card: #08080a;
    --ink: #ffffff;
    --ink-soft: #e6e6e6;
    --accent: #e31e26;
    --accent-dark: #9a1117;
  }
  * { margin: 0; padding: 0; box-sizing: border-box; }
  html, body {
    width: 1200px; height: 862px; overflow: hidden;
    background: var(--backdrop);
    font-family: "Source Sans 3", "Myriad Pro", Arial, sans-serif;
  }
  .stage {
    position: relative; width: 1200px; height: 862px;
    display: flex; justify-content: center; align-items: center; gap: 60px;
  }
  .card {
    position: relative; width: 300px; height: 525px;
    background: var(--card); color: var(--ink);
    border-bottom: 2px solid var(--accent);
    box-shadow: 0 14px 30px rgba(0,0,0,.25);
  }
  /* Front */
  .brand {
    position: absolute; top: 168px; left: 0; right: 0;
    text-align: center; font-weight: 700; font-size: 30px;
    line-height: 1.05; letter-spacing: 1px; text-transform: uppercase;
    color: var(--ink);
  }
  .divider {
    position: absolute; top: 274px; left: 30px; right: 30px; height: 2px;
    background: linear-gradient(90deg, transparent, var(--accent) 20%, var(--accent) 80%, transparent);
  }
  .slogan {
    position: absolute; top: 300px; left: 0; right: 0;
    text-align: center; font-weight: 700; font-style: italic;
    font-size: 15px; line-height: 1.3;
  }
  /* Back */
  .tie {
    position: absolute; top: 0; left: 160px; width: 50px; height: 250px;
    background: linear-gradient(180deg, var(--accent), var(--accent-dark));
  }
  .contact {
    position: absolute; top: 315px; left: 0; right: 0; text-align: center;
  }
  .contact-name { font-weight: 700; font-size: 21px; line-height: 1.1; }
  .contact-title { font-size: 14px; color: var(--ink-soft); margin-bottom: 14px; }
  .contact-address { font-size: 14px; line-height: 1.3; color: var(--ink-soft); margin-bottom: 12px; }
  .contact-phone {
    font-size: 14px; color: var(--ink-soft);
    display: inline-flex; align-items: center; gap: 5px;
  }
  .contact-phone svg { width: 13px; height: 13px; fill: var(--ink); }
  .website {
    position: absolute; bottom: 26px; left: 0; right: 0;
    text-align: center; font-size: 14px; color: var(--ink-soft);
  }
</style>
</head>
<body>
<main class="stage">
  <section class="card card-front">
    <h1 class="brand">Granary<br>Coat Mart</h1>
    <div class="divider"></div>
    <p class="slogan">Warehouse Selection,<br>Outlet Prices,<br>Outstanding Service.</p>
  </section>

  <section class="card card-back">
    <div class="tie" role="img" aria-label="Red necktie illustration hanging from the top edge"></div>
    <div class="contact">
      <p class="contact-name">Peter Olund</p>
      <p class="contact-title">Sales Associate</p>
      <p class="contact-address">418 E. Mirabeth Ave.<br>Gardena, CA 90247</p>
      <p class="contact-phone">
        <svg viewBox="0 0 24 24" aria-hidden="true"><path d="M2 8c0-3 4-5 10-5s10 2 10 5v2h-5V8c0-1-2-1.5-5-1.5S7 7 7 8v2H2zM6 12h12l3 8H3z"/></svg>
        310.555.0182
      </p>
    </div>
    <p class="website">www.granarycoatmart.example</p>
  </section>
</main>
</body>
</html>
```